Velvet Fern Beauty Bar Business Card

We need a modern, elegant business card design for our new beauty bar located in La Quinta, CA. The card should feel premium yet approachable, reflecting our brand identity: warm, stylish, and confidence-boosting.

Use our existing Velvet Fern Beauty Bar logo (to be provided as vector file).

Colors: Black, White, Blush / Nude accents, and Gold (metallic or foil effect if possible).

Typography: Clean sans-serif for clarity, with optional elegant script accent.
Design Style

Minimalist and modern with plenty of white space.

Premium look with a beauty/lifestyle feel (not overly corporate).

Option to explore vertical or horizontal orientation.

Rounded corners welcome, but not required.

Additional Notes

Design should print well in both matte and glossy finishes.

Please present mockups with both light and dark backgrounds.

Keep overall feel sleek, feminine, and high-end while still being approachable.

```html
<!DOCTYPE html>
<html lang="en">
<head>
<meta charset="utf-8">
<title>Velvet Fern Beauty Bar – Business Card</title>
<link rel="stylesheet" href="https://fonts.googleapis.com/css2?family=Jost:wght@400;500;600&display=swap">
<style>
  :root {
    --backdrop: #1b1a1a;
    --card-nude: #f4dfcf;
    --ink: #231f1e;
    --ink-soft: #3a3432;
    --foil-silver: #8f8a88;
    --decor-tone: #dccbbd;
  }
  * { margin: 0; padding: 0; box-sizing: border-box; }
  html, body {
    width: 1200px;
    height: 1186px;
    overflow: hidden;
    background: var(--backdrop);
    font-family: "Jost", sans-serif;
  }
  .canvas {
    position: relative;
    width: 1200px;
    height: 1186px;
  }
  .card {
    position: absolute;
    left: 205px;
    width: 760px;
    height: 433px;
    background: var(--card-nude);
    border-radius: 26px;
    overflow: hidden;
    box-shadow: 0 6px 18px rgba(0,0,0,0.45);
  }
  .card--front { top: 114px; }
  .card--back  { top: 618px; }

  .front-decor {
    position: absolute;
    right: 0;
    top: 60px;
    width: 380px;
    height: 373px;
    background: radial-gradient(ellipse at 60% 55%, rgba(220,203,189,0.75) 0%, rgba(220,203,189,0.25) 50%, rgba(244,223,207,0) 75%);
  }

  .brand-name {
    position: absolute;
    color: var(--ink);
    font-weight: 500;
    letter-spacing: 0.02em;
    white-space: nowrap;
    display: flex;
    align-items: center;
  }
  .brand-name .brand-dot {
    display: inline-block;
    border-radius: 50%;
    background: currentColor;
  }
  .card--front .brand-name {
    left: 38px;
    top: 100px;
    font-size: 40px;
    gap: 14px;
  }
  .card--front .brand-dot { width: 14px; height: 14px; }

  .contact {
    position: absolute;
    left: 30px;
    top: 272px;
    color: var(--ink);
  }
  .contact__name {
    font-size: 25px;
    font-weight: 600;
    letter-spacing: 0.01em;
    margin-left: 3px;
  }
  .contact__role {
    font-size: 17px;
    font-weight: 400;
    color: var(--ink-soft);
    margin-left: 3px;
    margin-top: -2px;
  }
  .contact__phone {
    font-size: 16px;
    margin-top: 18px;
    margin-left: 4px;
    letter-spacing: 0.03em;
  }
  .contact__web {
    font-size: 17px;
    margin-top: 6px;
    letter-spacing: 0.01em;
  }

  .card--back .brand-name {
    left: 0;
    right: 0;
    top: 0;
    bottom: 0;
    justify-content: center;
    font-size: 46px;
    color: var(--foil-silver);
    gap: 16px;
  }
  .card--back .brand-dot { width: 16px; height: 16px; }
</style>
</head>
<body>
<div class="canvas">
  <section class="card card--front">
    <div class="front-decor" role="img" aria-label="Faint large line-art profile decoration from the brand mark"></div>
    <div class="brand-name"><span class="brand-dot"></span>Velvet Fern Beauty Bar</div>
    <div class="contact">
      <p class="contact__name">Nora Whitfield</p>
      <p class="contact__role">SkinCare Specialist</p>
      <p class="contact__phone">+1 555-014-2290</p>
      <p class="contact__web">www.velvetfernbeauty.com</p>
    </div>
  </section>

  <section class="card card--back">
    <div class="brand-name"><span class="brand-dot"></span>Velvet Fern Beauty Bar</div>
  </section>
</div>
</body>
</html>
```